Stationary package for Health Care company

COMPANY NAME: Vantorel.
We have a company logo. We need to create a stationary package for a new health care company. The package needs to be unique, high tech, innovative (perhaps a folded business card, or something with a die-cut). It needs to be memorable.

The company makes in-home allergy test kits - customer takes an allergy test at home (with special medical device found in the kit) then, they send in their blood samples, and the company sends back a detailed report of what they are/are not allergic to.

We need:
business cards
thank you cards
labels
stationary
envelope
9" x 12" Pocket folder

Vantorel (The company) has a brochure for the product (called Mirodane). The stationary package should compliment the brochure. The brochure will reside in the pocket folder and they must look good together. Brochure uploaded. Note: the brochure is flat. Once folded - all you will actually see in the pocket folder is the cover with the man with outstretched arms.

INFO TO BE USED ON STATIONARY: DO NOT TRY AND CONTACT THIS PERSON!

Peter J. Harwick
Chief Executive Officer
48 Orland Commerce Parkway #210
Fernhollow ST 00071
Phone: 555-555-0172
Web site: www.vantorel-example.com
email: pharwick@vantorel-example.com
Updates

I have added all of the information to be used on the stationary package. PLEASE DO NOT TRY TO CONTACT THIS PERSON OR COMPANY. If you have any questions - contact me. Thank you. Owen

I've uploaded a cleaned up version of the Vantorel logo as a 300 dpi PSD if anyone needs it. Thank you. Owen

Target Market(s)

Doctors, hospitals, laboratories.

Industry/Entity Type

Medical

Requirements
Must have
• Must be memorable, high-tech. Must work together with Mirodane brochure. Descriptive words: freedom, breathe, clean, fresh

```html
<!DOCTYPE html>
<html lang="en">
<head>
<meta charset="utf-8">
<title>Vantorel Letterhead</title>
<link rel="stylesheet" href="https://fonts.googleapis.com/css2?family=Arimo:wght@400;700&display=swap">
<style>
  :root {
    --paper: #ffffff;
    --brand: #4b4f9e;
    --brand-light: #8a8fd0;
    --ink: #3f3f46;
    --icon: #5a5fb0;
  }
  * { margin: 0; padding: 0; box-sizing: border-box; }
  html, body {
    width: 800px;
    height: 1200px;
    overflow: hidden;
    background: var(--paper);
  }
  .letterhead {
    position: relative;
    width: 800px;
    height: 1200px;
    background: var(--paper);
    font-family: "Arimo", Arial, sans-serif;
    color: var(--ink);
  }
  .brand {
    position: absolute;
    left: 46px;
    top: 100px;
    display: flex;
    align-items: center;
    gap: 14px;
  }
  .brand-dot {
    width: 30px;
    height: 30px;
    border-radius: 50%;
    background: var(--brand-light);
  }
  .brand-name {
    font-size: 58px;
    font-weight: 400;
    color: var(--brand);
    letter-spacing: -0.5px;
    line-height: 1;
  }
  .contact {
    position: absolute;
    left: 574px;
    top: 74px;
    list-style: none;
    font-size: 12px;
    line-height: 15px;
    white-space: nowrap;
  }
  .contact li {
    display: flex;
    align-items: flex-start;
    gap: 10px;
    margin-bottom: 9px;
  }
  .contact svg {
    flex: none;
    width: 15px;
    height: 15px;
    fill: var(--icon);
  }
  .web {
    position: absolute;
    left: 574px;
    top: 1124px;
    display: flex;
    align-items: center;
    gap: 10px;
    font-size: 12px;
    font-weight: 700;
    color: var(--ink);
    white-space: nowrap;
  }
  .web svg { width: 15px; height: 15px; flex: none; }
</style>
</head>
<body>
  <main class="letterhead">
    <div class="brand">
      <span class="brand-dot"></span>
      <span class="brand-name">Vantorel</span>
    </div>

    <ul class="contact">
      <li>
        <svg viewBox="0 0 16 16" aria-hidden="true"><path d="M2 6c0-2 2.5-3 6-3s6 1 6 3l-2.5 1-1-1.5h-5l-1 1.5zM4 8h8l1 5H3z"/></svg>
        <span>555-555-0172</span>
      </li>
      <li>
        <svg viewBox="0 0 16 16" aria-hidden="true"><path d="M1 3h14v10H1zM2.5 4.5 8 9l5.5-4.5v-.2H2.5z" fill-rule="evenodd"/></svg>
        <span>pharwick@vantorel-example.com</span>
      </li>
      <li>
        <svg viewBox="0 0 16 16" aria-hidden="true"><path d="M8 1a5 5 0 0 1 5 5c0 4-5 9-5 9S3 10 3 6a5 5 0 0 1 5-5zm0 3a2 2 0 1 0 0 4 2 2 0 0 0 0-4z" fill-rule="evenodd"/></svg>
        <span>48 Orland Commerce Parkway #210<br>Fernhollow ST 00071</span>
      </li>
    </ul>

    <div class="web">
      <svg viewBox="0 0 16 16" aria-hidden="true">
        <circle cx="8" cy="8" r="7" fill="var(--icon)"/>
        <ellipse cx="8" cy="8" rx="3" ry="7" fill="none" stroke="#fff" stroke-width="1"/>
        <line x1="1" y1="8" x2="15" y2="8" stroke="#fff" stroke-width="1"/>
      </svg>
      <span>www.vantorel-example.com</span>
    </div>
  </main>
</body>
</html>
```